Breakfast Briefings / Lunch & Learn

I would like to have a double sided flyer size 8x10 to display the breakfast briefing on one side and Lunch & Learn on the other side.

Header on each side to say
2018 Calendar Breakfast Briefing (on the breakfast side)
2018 Calendar Lunch & Learn (on the lunch side)

I have attached a copy of the files we would like to use.

Learn

```html
<!DOCTYPE html>
<html lang="en">
<head>
<meta charset="utf-8">
<title>2018 Calendar Breakfast Briefing</title>
<link rel="stylesheet" href="https://fonts.googleapis.com/css2?family=Arimo:wght@400;700&family=Nunito:wght@800;900&display=swap">
<style>
  :root {
    --sky: #a8c8e6;
    --sky-deep: #95bbe0;
    --navy: #1a6fae;
    --navy-dark: #15609a;
    --badge-fill: #a9cdea;
    --pale: #dce9f5;
    --white: #ffffff;
    --ink: #17334f;
  }
  html, body {
    margin: 0;
    padding: 0;
    overflow: hidden;
  }
  .flyer {
    position: relative;
    width: 960px;
    height: 1200px;
    overflow: hidden;
    background: linear-gradient(180deg, var(--sky) 0%, var(--sky-deep) 100%);
    font-family: "Arimo", Arial, sans-serif;
  }
  .backdrop {
    position: absolute;
    inset: 0;
  }
  .title-block {
    position: absolute;
    left: 0;
    top: 0;
    color: var(--white);
    font-family: "Nunito", "Arial Rounded MT Bold", sans-serif;
  }
  .title-year {
    position: absolute;
    left: 62px;
    top: 268px;
    transform: rotate(-90deg);
    transform-origin: left top;
    font-weight: 900;
    font-size: 72px;
    letter-spacing: 3px;
    line-height: 1;
  }
  .title-rule {
    position: absolute;
    left: 150px;
    top: 48px;
    width: 4px;
    height: 218px;
    background: var(--white);
  }
  .title-kicker {
    position: absolute;
    left: 162px;
    top: 36px;
    font-weight: 900;
    font-size: 54px;
    line-height: 1;
  }
  .title-main {
    position: absolute;
    left: 160px;
    top: 96px;
    margin: 0;
    font-weight: 900;
    font-size: 98px;
    line-height: 0.95;
    letter-spacing: -1px;
  }
  .feature-photo {
    position: absolute;
    left: 302px;
    top: 564px;
    width: 356px;
    height: 356px;
    border-radius: 50%;
    background: linear-gradient(160deg, #8f6c4d 0%, #a8865f 35%, #cdbba6 65%, #efebe6 100%);
  }
  .badge {
    position: absolute;
    box-sizing: border-box;
    width: 128px;
    height: 128px;
    margin: -64px 0 0 -64px;
    border: 6px solid var(--navy);
    border-radius: 50%;
    background: var(--badge-fill);
    display: flex;
    flex-direction: column;
    align-items: center;
    justify-content: center;
    text-align: center;
    color: var(--ink);
  }
  .badge-dept {
    font-weight: 700;
    font-size: 15px;
    line-height: 1.05;
    padding-bottom: 3px;
    border-bottom: 2px solid var(--navy);
    min-width: 88px;
  }
  .badge-dept.small {
    font-size: 11px;
  }
  .badge-name {
    font-weight: 700;
    font-size: 16px;
    line-height: 1.12;
    padding: 3px 0;
    border-bottom: 2px solid var(--navy);
    min-width: 88px;
  }
  .badge-month {
    font-weight: 700;
    font-size: 14px;
    padding-top: 3px;
  }
</style>
</head>
<body>
<main class="flyer">
  <svg class="backdrop" width="960" height="1200" viewBox="0 0 960 1200" aria-hidden="true">
    <circle cx="960" cy="100" r="330" fill="none" stroke="var(--pale)" stroke-width="2"/>
    <circle cx="960" cy="100" r="240" fill="none" stroke="var(--pale)" stroke-width="2"/>
    <circle cx="480" cy="742" r="500" fill="none" stroke="var(--navy)" stroke-width="2" opacity="0.7"/>
    <circle cx="480" cy="742" r="475" fill="var(--pale)" opacity="0.5"/>
    <circle cx="480" cy="742" r="430" fill="var(--white)" opacity="0.55"/>
    <circle cx="250" cy="-80" r="410" fill="var(--navy)"/>
    <circle cx="250" cy="-80" r="430" fill="none" stroke="var(--navy)" stroke-width="2"/>
    <circle cx="905" cy="67" r="57" fill="var(--navy)"/>
    <circle cx="480" cy="742" r="205" fill="var(--navy-dark)"/>
    <circle cx="480" cy="742" r="188" fill="var(--white)"/>
  </svg>

  <header class="title-block">
    <div class="title-year">2018</div>
    <div class="title-rule"></div>
    <div class="title-kicker">Calendar</div>
    <h1 class="title-main">Breakfast<br>Briefing</h1>
  </header>

  <div class="feature-photo" role="img" aria-label="Photo of a breakfast table with a tablet showing the 2018 calendar of breakfast briefings, coffee, orange juice and pastries"></div>

  <section class="badge" style="left:508px;top:430px">
    <div class="badge-dept">Medical</div>
    <div class="badge-name">Daniel<br>Carver</div>
    <div class="badge-month">2019</div>
  </section>
  <section class="badge" style="left:647px;top:465px">
    <div class="badge-dept">Sales</div>
    <div class="badge-name">Jon<br>Aldren</div>
    <div class="badge-month">2019</div>
  </section>
  <section class="badge" style="left:783px;top:590px">
    <div class="badge-dept">Finance</div>
    <div class="badge-name">Ray<br>Calder</div>
    <div class="badge-month">March</div>
  </section>
  <section class="badge" style="left:840px;top:752px">
    <div class="badge-dept">R&amp;D</div>
    <div class="badge-name">Chris<br>Constantin</div>
    <div class="badge-month">April</div>
  </section>
  <section class="badge" style="left:797px;top:917px">
    <div class="badge-dept">Operations</div>
    <div class="badge-name">Peter<br>Schultz</div>
    <div class="badge-month">May</div>
  </section>
  <section class="badge" style="left:675px;top:1050px">
    <div class="badge-dept">Clinical/Reg</div>
    <div class="badge-name">Brett<br>Glover</div>
    <div class="badge-month">June</div>
  </section>
  <section class="badge" style="left:533px;top:1100px">
    <div class="badge-dept">Quality</div>
    <div class="badge-name">Dennis<br>Albrecht</div>
    <div class="badge-month">July</div>
  </section>
  <section class="badge" style="left:353px;top:1050px">
    <div class="badge-dept">People</div>
    <div class="badge-name">Diya<br>Ghosal</div>
    <div class="badge-month">August</div>
  </section>
  <section class="badge" style="left:250px;top:933px">
    <div class="badge-dept">Marketing</div>
    <div class="badge-name">Nikhil<br>Tandon</div>
    <div class="badge-month">September</div>
  </section>
  <section class="badge" style="left:183px;top:763px">
    <div class="badge-dept">Legal</div>
    <div class="badge-name">Karim<br>Rahman</div>
    <div class="badge-month">October</div>
  </section>
  <section class="badge" style="left:230px;top:597px">
    <div class="badge-dept small">Marketing<br>Access</div>
    <div class="badge-name">Kristen<br>Neumann</div>
    <div class="badge-month">November</div>
  </section>
  <section class="badge" style="left:363px;top:472px">
    <div class="badge-dept">TOS</div>
    <div class="badge-name">Clara<br>Stone</div>
    <div class="badge-month">December</div>
  </section>
</main>
</body>
</html>
```